School/Team Fundraiser Pillow Promotion

We need to design a product card that will draw attention to this fundraiser. Imagine a sports team selling natural latex pillows to raise funds for their team. This card will be inserted into the pillow package. Each pillow costs $50. The customer will also receive $50 off any purchase in our stores if they bring the card with them at time of purchase.

Target Market(s)

Parents of School and Youth Sports Teams

Industry/Entity Type

Retail

Font styles to use
Serif

Colors
3176b5
85abd2
0356a4

Requirements
Must have
• Design must match our style. See velvetrestbedding.example or attached style guide.
• Size 8.5"x11"
• $50 price point.
• Bullet Points: (Feel free to condense)
• Soft shredded natural latex
• Contours to your unique head and neck shape
• Shredded latex is all natural
• Hypoallergenic
• No off-gassing chemicals
• Dust Mite Resistant
• Mold Resistant
• Natural Latex is breathable and provides a cooler nights sleep
• Made locally in the USA
• Fundraiser pillow. By purchasing you are supporting ? Team/School
• I need to be able to swap out school/team logo.
• ** Please see style guide for colors and fonts **
• Please use Arno Pro as main font.
Nice to have
• I like the excitement in these images...
• https://pixlink.example/images/q7Rm2T
• https://pixlink.example/images/h3Kp8Z
• https://pixlink.example/images/LwYb4N
• https://pixlink.example/images/fa9Jv6
Should not have
• Sexual inudndo

```html
<!DOCTYPE html>
<html lang="en">
<head>
<meta charset="utf-8">
<title>Shredded Latex Pillow – Fundraiser Card</title>
<link rel="stylesheet" href="https://fonts.googleapis.com/css2?family=Crimson+Pro:wght@400;500&display=swap">
<style>
  :root {
    --navy: #223247;
    --stone: #787272;
    --paper: #ffffff;
    --ink-light: #f2f2f2;
    --photo-top: #e9ebee;
    --photo-mid: #a6acb6;
    --photo-low: #5f6672;
  }
  * { margin: 0; padding: 0; box-sizing: border-box; }
  html, body { width: 1200px; height: 1197px; overflow: hidden; background: var(--paper); }
  body { position: relative; font-family: "Crimson Pro", Georgia, serif; color: var(--ink-light); }

  .product-panel {
    position: absolute; left: 36px; top: 37px; width: 1127px; height: 871px;
    background: var(--navy);
  }
  .room-photo {
    position: absolute; left: 0; top: 0; width: 828px; height: 684px;
    background: linear-gradient(160deg, var(--photo-top) 0%, #d3d7dd 35%, var(--photo-mid) 62%, var(--photo-low) 100%);
    border-right: 3px solid var(--paper);
    border-bottom: 3px solid var(--paper);
  }
  .price-corner { position: absolute; left: 669px; top: 0; width: 159px; height: 192px; }
  .price-corner-amount {
    position: absolute; right: 16px; top: 30px;
    font-size: 54px; line-height: 1; color: var(--paper);
  }
  .price-corner-amount sup, .gift-amount sup { font-size: 0.45em; vertical-align: 0.95em; margin-right: 2px; }

  .product-details { position: absolute; left: 864px; top: 36px; width: 250px; }
  .product-title { font-size: 38px; font-weight: 400; line-height: 45px; }
  .product-material { margin-top: 18px; font-size: 17px; line-height: 23px; }
  .feature-list { list-style: none; margin-top: 20px; font-size: 20px; line-height: 29px; }
  .feature-list li { position: relative; padding-left: 19px; margin-bottom: 8px; }
  .feature-list li::before { content: "•"; position: absolute; left: 0; top: 0; }

  .fundraiser-note {
    position: absolute; left: 864px; top: 698px; width: 240px;
    font-size: 20px; line-height: 29px;
  }
  .brand-name {
    position: absolute; left: 160px; top: 758px; width: 510px; text-align: center;
    font-size: 32px; letter-spacing: 4px; color: var(--paper); font-weight: 400;
  }

  .gift-card {
    position: absolute; top: 948px; width: 350px; height: 206px; text-align: center;
    color: var(--paper);
  }
  .gift-card--navy { left: 246px; background: var(--navy); }
  .gift-card--stone { left: 606px; background: var(--stone); }
  .gift-card-frame {
    position: absolute; left: 11px; top: 11px; right: 11px; bottom: 11px;
    border: 1px solid rgba(255,255,255,0.75);
  }
  .gift-amount { margin-top: 28px; font-size: 72px; line-height: 1; }
  .gift-label { margin-top: 2px; font-size: 25px; line-height: 28px; }
  .gift-terms { margin-top: 8px; font-size: 13.5px; line-height: 18px; }
  .gift-contact { margin-top: 8px; font-size: 10px; line-height: 14px; }
</style>
</head>
<body>
  <section class="product-panel">
    <div class="room-photo" role="img" aria-label="Bright master bedroom with a carved dark wood bed, striped grey bedding, pillows and a blue patterned rug"></div>
    <svg class="price-corner" viewBox="0 0 159 192" aria-hidden="true">
      <polygon points="0,0 159,0 159,192" fill="#787272"/>
    </svg>
    <div class="price-corner-amount" style="left:705px;right:auto;top:32px;position:absolute"><sup>$</sup>50</div>

    <p class="brand-name">VELVET REST BEDDING</p>
  </section>

  <div class="product-details" style="left:900px;top:72px">
    <h1 class="product-title">Shredded<br>Latex Pillow</h1>
    <p class="product-material">100% Natural Tree Based<br>Latex Rubber</p>
    <ul class="feature-list">
      <li>Contours to your unique head and neck shape</li>
      <li>Shredded latex is all natural</li>
      <li>Hypoallergenic</li>
      <li>No off-gassing chemicals</li>
      <li>Dust Mite Resistant</li>
      <li>Mold Resistant</li>
      <li>Natural Latex is breathable and provides a cooler nights sleep</li>
      <li>Made locally in the USA</li>
    </ul>
  </div>

  <p class="fundraiser-note" style="left:900px;top:735px">Fundraiser pillow.<br>By purchasing you<br>are supporting ?</p>

  <article class="gift-card gift-card--navy">
    <div class="gift-card-frame"></div>
    <p class="gift-amount"><sup>$</sup>50</p>
    <p class="gift-label">Gift Card</p>
    <p class="gift-terms">Towards the purchase of the Matters</p>
    <p class="gift-contact">velvetrestbedding.example | 555.014.0287</p>
  </article>

  <article class="gift-card gift-card--stone">
    <div class="gift-card-frame"></div>
    <p class="gift-amount"><sup>$</sup>50</p>
    <p class="gift-label">Gift Card</p>
    <p class="gift-terms">Towards the purchase of the Matters</p>
    <p class="gift-contact">velvetrestbedding.example | 555.014.0287</p>
  </article>
</body>
</html>
```